Website for IT consulting Company

I need a website upgrade, the existing site content is ok, I would also like to add a testimonial page, the site should be something that is easy for us to update content. You use the content from www.velmarketa.com as an example. I will also post update logo and artwork. I also need a contact form with some type of validation or captcha.

Please omit Address maps

Target Market(s)

small business, service oriented companies. We provide IT Consulting, support and mangement

Industry/Entity Type

Information Technology

Coding

Coded - Design and coding required

Number of Pages Required

1 page

Font styles to use
Serif
Sans Serif

Requirements
Must have
• Contain logo attached, and content from existing web site www.velmarketa.com.
• Also need to update content easily, and be movable to different platforms.
• There is a catch phrase
• "Let us worry about your technology…” “ so you don’t have to!”
• Should be included.
Nice to have
• Testimonial page, Project page where we can post new and past projects and pictures
Should not have
• none

```html
<!DOCTYPE html>
<html lang="en">
<head>
<meta charset="utf-8">
<title>Velmarketa Advisory Group – IT Solutions</title>
<link href="https://fonts.googleapis.com/css2?family=Ubuntu:wght@400;500;700&family=Roboto:wght@400;500&display=swap" rel="stylesheet">
<style>
:root{
  --blue:#1a9ad6;
  --blue-dark:#1466a6;
  --footer-bar:#1aa0dd;
  --ink:#1f1f1f;
  --text:#555b63;
  --pale:#eaf0f8;
  --white:#fff;
  --field-border:#cfd5dc;
}
*{box-sizing:border-box;margin:0;padding:0}
html,body{width:1200px;height:3125px;overflow:hidden}
body{font-family:"Roboto",Arial,sans-serif;color:var(--text);background:var(--white);position:relative}
.abs{position:absolute}
.heading{font-family:"Ubuntu",Arial,sans-serif;font-weight:400;color:var(--ink);text-transform:uppercase;display:flex;align-items:center;gap:12px;white-space:nowrap}
.mark{display:block;width:26px;height:26px;flex:none;background:var(--blue)}
.read-more{font-family:"Ubuntu",sans-serif;font-size:17px;color:var(--ink);text-decoration:underline;font-weight:500}
.raquo{font-family:"Ubuntu",sans-serif;font-size:17px;color:var(--ink);font-weight:700;margin-left:4px}

/* hero */
.hero{left:0;top:0;width:1200px;height:640px;overflow:hidden}
.hero-photo{position:absolute;inset:0;background:linear-gradient(100deg,#2a2f38 0%,#5a6470 40%,#7e8a98 70%,#4f5b68 100%)}
.hero-header{position:absolute;left:0;top:0;width:1200px;height:112px;background:rgba(40,44,52,.55);border-bottom:2px solid var(--blue)}
.brand{position:absolute;left:78px;top:30px;display:flex;align-items:center;gap:12px;font-family:"Ubuntu",sans-serif;font-weight:700;font-size:42px;color:var(--white);letter-spacing:1px}
.brand-dot{width:40px;height:40px;background:var(--blue)}
.menu{position:absolute;right:74px;top:36px;display:flex;align-items:center;gap:12px;color:var(--white);font-family:"Ubuntu",sans-serif;font-size:22px}
.menu i{display:block;width:30px;height:4px;background:var(--white);box-shadow:0 9px 0 var(--white),0 -9px 0 var(--white)}
.hero-copy{position:absolute;right:80px;top:208px;text-align:right;font-family:"Ubuntu",sans-serif}
.hero-copy h1{color:var(--blue);font-weight:700;font-size:48px;line-height:66px;text-transform:uppercase}
.hero-copy p{color:var(--white);font-size:22px;margin-top:8px}
.hero-cut{position:absolute;left:0;bottom:0}

/* about */
.about-title{left:0;width:1200px;top:682px;justify-content:center;font-size:40px}
.about-text{left:150px;width:900px;top:752px;text-align:center;font-size:13.5px;line-height:25px}
.about-more{left:0;width:1200px;top:830px;text-align:center}
.services{left:40px;width:1120px;top:905px;display:flex;align-items:flex-start}
.arrow{font-size:34px;color:var(--ink);font-weight:700;width:38px;margin-top:75px}
.service{width:348px;margin-right:16px}
.service:last-of-type{margin-right:0}
.service-head{display:flex;align-items:center;gap:16px;height:58px}
.service-head svg{width:50px;height:50px;flex:none}
.service h3{font-family:"Ubuntu",sans-serif;font-weight:400;font-size:19px;line-height:25px;color:var(--blue)}
.service.first h3{color:var(--ink)}
.service p{font-size:14.5px;line-height:23px;margin-top:6px}
.service .read-more{display:block;margin-top:4px;font-size:16px}
.service:not(.first) .read-more{color:var(--blue);text-decoration:none}

/* support */
.support{left:0;top:1124px;width:1200px;height:792px;background:linear-gradient(180deg,#eef3fa,#f7f9fc 60%,#fff)}
.photo{position:absolute}
.support-photo{left:77px;top:32px;width:523px;height:334px;background:linear-gradient(135deg,#0b1640,#1c3b8a 55%,#0d1a45)}
.support-title{right:80px;top:24px;font-size:28px;justify-content:flex-end}
.support-title .mark,.out-title .mark{width:22px;height:22px}
.support-text{right:80px;top:74px;width:500px;text-align:right;font-size:14.5px;line-height:24px}
.support-list{left:660px;top:162px;display:grid;grid-template-columns:255px 200px;row-gap:20px;font-size:15.5px;color:#333}
.support-list li{list-style:none;display:flex;align-items:center;gap:10px}
.support-list svg{width:22px;height:22px;flex:none}
.out-title{left:77px;top:422px;font-size:28px}
.out-text{left:77px;top:474px;width:470px;font-size:14.5px;line-height:24px}
.out-more{left:77px;top:602px}
.out-photo{left:600px;top:428px;width:521px;height:333px;background:linear-gradient(135deg,#c7cdd4,#e4e8ec 50%,#9aa6b4)}

/* testimonial */
.test-title{left:0;width:1200px;top:1972px;justify-content:center;font-size:40px}
.test-sub{left:0;width:1200px;top:2046px;text-align:center;font-size:14px}
.quote-mark{left:218px;top:2068px}
.quote{left:208px;top:2088px;width:782px;height:124px;border-radius:8px;color:var(--white);padding:34px 30px 0 40px;font-size:14.5px;line-height:25px;background:linear-gradient(180deg,#1f7cc4,#1667ab)}
.quote-tail{left:255px;top:2210px}
.client{left:300px;top:2220px;font-family:"Ubuntu",sans-serif;font-size:16px;color:var(--ink)}
.dots{left:538px;top:2262px;display:flex;gap:4px}
.dots span{width:16px;height:16px;border:2px solid var(--blue-dark)}
.dots span.on{background:var(--blue-dark)}

/* contact */
.contact{left:0;top:2343px;width:1200px;height:434px;background:var(--pale)}
.contact-title{left:0;width:1200px;top:44px;justify-content:center;font-size:40px}
.field{position:absolute;background:var(--white);border:1px solid var(--field-border);font-size:14px;color:#666;padding:0 14px;display:flex;align-items:center}
.f1{left:94px;top:118px;width:312px;height:50px}
.f2{left:432px;top:118px;width:310px;height:50px}
.f3{left:760px;top:118px;width:345px;height:50px}
.f4{left:94px;top:192px;width:1011px;height:126px;align-items:flex-start;padding-top:16px}
.send{position:absolute;left:529px;top:336px;width:142px;height:50px;background:var(--blue);color:var(--white);font-family:"Ubuntu",sans-serif;font-size:18px;display:flex;align-items:center;justify-content:center;border-radius:2px}

/* footer */
.footer{left:0;top:2777px;width:1200px;height:296px;background:linear-gradient(90deg,#115696,#1b6eb2)}
.col{position:absolute;top:50px;color:var(--white)}
.col h4{font-family:"Ubuntu",sans-serif;font-weight:400;font-size:19px;letter-spacing:.5px;margin-bottom:22px}
.links{left:78px}
.links li{list-style:none;font-size:14.5px;line-height:25px}
.news{left:456px;width:260px}
.news p{font-size:15px;line-height:24px;color:#9fc4e6}
.news-input{margin-top:22px;width:256px;border-bottom:1px solid #9fc4e6;height:30px;display:flex;justify-content:space-between;align-items:center;font-size:13px;color:#9fc4e6;padding:0 6px 0 10px}
.news-btn{margin:10px 0 0 50px;width:162px;height:40px;background:var(--white);color:var(--blue-dark);font-family:"Ubuntu",sans-serif;font-size:18px;display:flex;align-items:center;justify-content:center}
.reach{left:815px;width:320px}
.reach li{list-style:none;display:flex;gap:14px;font-size:14.5px;line-height:24px;margin-bottom:16px}
.reach svg{width:20px;height:20px;flex:none;margin-top:2px}
.bottom-bar{left:0;top:3073px;width:1200px;height:52px;background:var(--footer-bar);color:var(--white);font-size:15px}
.copy{position:absolute;left:78px;top:16px}
.copy b{color:#0c2f57;font-weight:500}
.social{position:absolute;right:78px;top:5px;display:flex;gap:14px}
.social span{width:42px;height:42px;border-radius:50%;background:var(--white)}
</style>
</head>
<body>

<header class="hero abs">
  <div class="hero-photo" role="img" aria-label="Photo of a smiling businesswoman typing on a laptop in an office"></div>
  <div class="hero-header">
    <div class="brand"><span class="brand-dot"></span>VELMARKETA</div>
    <div class="menu">MENU <i></i></div>
  </div>
  <div class="hero-copy">
    <h1>IT Solutions that work<br>for your business.</h1>
    <p>A full service technology company</p>
  </div>
  <svg class="hero-cut" width="1200" height="140" viewBox="0 0 1200 140">
    <path d="M0 140 L0 132 C300 120 560 70 760 40 C900 20 1060 6 1200 0 L1200 140 Z" fill="#fff"/>
  </svg>
</header>

<h2 class="heading abs about-title"><span class="mark"></span>About Us</h2>
<p class="abs about-text">Velmarketa Advisory Group, Inc. was established in 1991. Our mission is helping businesses and individuals realize a Return on Investment by implementing today's advanced technologies. As a small business we understand the importance of technology and personalized attention.Every member of our support team has worked with both large and small companies...</p>
<div class="abs about-more"><span class="read-more">READ MORE</span><span class="raquo">»</span></div>

<section class="abs services">
  <div class="arrow">«</div>
  <div class="service first">
    <div class="service-head">
      <svg viewBox="0 0 50 50"><circle cx="18" cy="20" r="11" fill="none" stroke="#1a9ad6" stroke-width="5" stroke-dasharray="4 3"/><circle cx="18" cy="20" r="4" fill="#1466a6"/><rect x="8" y="36" width="36" height="8" rx="2" fill="#1466a6"/><circle cx="36" cy="30" r="5" fill="#1a9ad6"/></svg>
      <h3>Managed IT Solutions</h3>
    </div>
    <p>Our staff will design, service, administer and maintain your IT needs. We are well versed on all major operating system...</p>
    <span class="read-more">READ MORE »</span>
  </div>
  <div class="service">
    <div class="service-head">
      <svg viewBox="0 0 50 50"><rect x="6" y="8" width="38" height="26" rx="2" fill="none" stroke="#333" stroke-width="3"/><rect x="18" y="36" width="14" height="4" fill="#333"/><rect x="12" y="40" width="26" height="4" fill="#333"/><circle cx="25" cy="21" r="7" fill="none" stroke="#1a9ad6" stroke-width="3"/></svg>
      <h3>Remote Diagnostic and Support</h3>
    </div>
    <p>Do you need a quick solution to a technical problem? With our live remote-assistance tool, a member of our support team...</p>
    <span class="read-more">READ MORE »</span>
  </div>
  <div class="service">
    <div class="service-head">
      <svg viewBox="0 0 50 50"><rect x="6" y="6" width="26" height="34" fill="none" stroke="#333" stroke-width="3"/><line x1="11" y1="14" x2="27" y2="14" stroke="#333" stroke-width="2"/><line x1="11" y1="20" x2="27" y2="20" stroke="#333" stroke-width="2"/><rect x="24" y="22" width="20" height="20" fill="#fff" stroke="#1a9ad6" stroke-width="3"/><text x="34" y="37" font-size="11" text-anchor="middle" fill="#1466a6" font-family="Roboto,sans-serif">{}</text></svg>
      <h3>IT Infrastructure Design and Installation</h3>
    </div>
    <p>Do you have more than one site? Do you need remote access? We can design and implement LANS/WANS and VPN's...</p>
    <span class="read-more">READ MORE »</span>
  </div>
  <div class="arrow" style="margin-left:14px">»</div>
</section>

<section class="abs support">
  <div class="photo support-photo" role="img" aria-label="Photo of a technician at a keyboard surrounded by security keywords on a dark blue screen"></div>
  <h2 class="heading abs support-title"><span class="mark"></span>IT Support Solutions</h2>
  <p class="abs support-text">Velmarketa is a technology solution provider based in Austin, Texas.Velmarketa has the experience, the tools, high-level technology solutions and training to power your business and your work force.</p>
  <ul class="abs support-list">
    <li><svg viewBox="0 0 22 22"><path d="M4 16 a5 5 0 0 1 2-9 a6 6 0 0 1 11 2 a4 4 0 0 1 0 7z" fill="#1a9ad6"/></svg>Network Asministration</li>
    <li><svg viewBox="0 0 22 22"><circle cx="11" cy="12" r="2" fill="#1466a6"/><path d="M6 7 a7 7 0 0 0 0 10 M16 7 a7 7 0 0 1 0 10" fill="none" stroke="#1a9ad6" stroke-width="2"/><line x1="11" y1="14" x2="11" y2="21" stroke="#1466a6" stroke-width="2"/></svg>Wireless Network</li>
    <li><svg viewBox="0 0 22 22"><path d="M11 2 L19 5 V11 C19 16 15 19 11 21 C7 19 3 16 3 11 V5 Z" fill="#1a9ad6"/></svg>Antivirus Solution</li>
    <li><svg viewBox="0 0 22 22"><path d="M3 18 L10 11 M12 9 L19 3" stroke="#1466a6" stroke-width="3"/><circle cx="11" cy="10" r="3" fill="#1a9ad6"/></svg>Network cabling</li>
    <li><svg viewBox="0 0 22 22"><circle cx="11" cy="11" r="3" fill="#1466a6"/><circle cx="4" cy="5" r="2.5" fill="#1a9ad6"/><circle cx="18" cy="5" r="2.5" fill="#1a9ad6"/><circle cx="11" cy="19" r="2.5" fill="#1a9ad6"/><path d="M4 5 L11 11 L18 5 M11 11 V19" stroke="#1a9ad6" stroke-width="1.5"/></svg>Network Security</li>
    <li><svg viewBox="0 0 22 22"><rect x="2" y="3" width="18" height="12" rx="1" fill="none" stroke="#1466a6" stroke-width="2"/><rect x="8" y="16" width="6" height="3" fill="#1a9ad6"/></svg>Desktop Support</li>
  </ul>
  <h2 class="heading abs out-title"><span class="mark"></span>Outsourcing Technology</h2>
  <p class="abs out-text">In today's world, companies are expected to use technology to function and stay competitive. However, this aspect of business provides many challenges that most companies cannot solve on their own. Outsourcing technology provides solutions to almost every aspect of your business and can increase your profits.</p>
  <div class="abs out-more"><span class="read-more">READ MORE</span><span class="raquo">»</span></div>
  <div class="photo out-photo" role="img" aria-label="Photo of two colleagues smiling at a computer monitor in a bright office"></div>
</section>

<h2 class="heading abs test-title"><span class="mark"></span>Testimonial</h2>
<p class="abs test-sub">What People Say About Orwell &amp; Pike, P.C from Our Customer</p>
<svg class="abs quote-mark" width="56" height="40" viewBox="0 0 56 40"><path d="M4 38 V22 C4 10 10 4 22 2 V10 C14 12 12 16 12 22 H22 V38Z M32 38 V22 C32 10 38 4 50 2 V10 C42 12 40 16 40 22 H50 V38Z" fill="#7fb6e0" opacity=".6"/></svg>
<div class="abs quote">"Lorem Ipsum is simply dummy text of the printing and typesetting industry. Lorem Ipsum has been the industry's standard dummy text ever since the 1500s, when an unknown printer took a galley of type and scrambled it to make a type specimen book."</div>
<svg class="abs quote-tail" width="30" height="28" viewBox="0 0 30 28"><path d="M0 0 H30 L28 28 Z" fill="#1667ab"/></svg>
<p class="abs client">-Client Name</p>
<div class="abs dots"><span></span><span class="on"></span><span></span><span></span><span></span><span></span></div>

<section class="abs contact">
  <h2 class="heading abs contact-title"><span class="mark"></span>Quick Contact</h2>
  <div class="field f1">Enter Name</div>
  <div class="field f2">Enter Email</div>
  <div class="field f3">Enter Contact No.</div>
  <div class="field f4">Enter Name</div>
  <div class="send">SEND</div>
</section>

<footer class="abs footer">
  <div class="col links">
    <h4>USEFULL LINKS</h4>
    <ul><li>Home</li><li>About</li><li>Services</li><li>Careers</li><li>Solution</li><li>Contact</li></ul>
  </div>
  <div class="col news">
    <h4>NEWSLETTER</h4>
    <p>Lorem Ipsum is simply dummy text of the printing and typesetting.</p>
    <div class="news-input">Email Id <svg width="20" height="18" viewBox="0 0 20 18"><path d="M1 8 L19 1 L14 17 L9 11 Z M9 11 L19 1" fill="none" stroke="#fff" stroke-width="1.5"/></svg></div>
    <div class="news-btn">SUBMIT</div>
  </div>
  <div class="col reach">
    <h4>CONTACT US</h4>
    <ul>
      <li><svg viewBox="0 0 20 20"><path d="M10 1 V19 M3 4 H15 L17 6 L15 8 H3 Z M5 10 H17 V14 H5 L3 12 Z" fill="#fff" stroke="#fff" stroke-width="1"/></svg><span>Velmarketa Advisory Group, Inc.<br>418 Harlow Ave.<br>Austin, Texas 78704</span></li>
      <li><svg viewBox="0 0 20 20"><path d="M5 2 L8 6 L6 8 C7 11 9 13 12 14 L14 12 L18 15 L16 18 C9 18 2 11 2 4 Z" fill="#fff"/></svg><span>(512) 555-0148</span></li>
      <li><svg viewBox="0 0 20 20"><rect x="2" y="5" width="16" height="11" fill="#fff"/><path d="M2 5 L10 11 L18 5" fill="none" stroke="#1763a3" stroke-width="1.5"/></svg><span>info@velmarketa.com</span></li>
    </ul>
  </div>
</footer>
<div class="abs bottom-bar">
  <p class="copy">© <b>Velmarketa Advisory Group,Inc.</b> - 2017 All Right Reserved</p>
  <div class="social"><span></span><span></span><span></span></div>
</div>

</body>
</html>
```